MY BEST MARKETING TOOL 8 PAGE FULL COLOR BOOKLET TO PHYSICIANS

I HAVE CORRECT DATA IN RIGHT PLACES. NEED HELP WITH FINISHING TOUCHES TO MAKE IT LOOK PROFESSIONAL AND GET IT PRINT READY. I HAVE USED CANVA TO GET THIS FAR. SO IF I NEED TO SHARE CANVA WITH YOU, HAPPY TO DO SO. THESE BOOKLETS WILL BE USED IN MARKETING. AUDIENCE IS DOCTORS. I WANT INFO TO BE CLEAR AND EASY TO FOLLOW.
Updates

MY FAVORITE COLORS ARE NAVY BLUE, COLUMBIA (SKY BLUE), LIGHT GRAY, SILVER, AND WHITE. THINK THESE SHOULD BE BASIC COLOR RANGE.

TRY TO USE LARGER TEXT PLEASE.

WEBSITE FOR BUSINESS---------------CAREHALO918.COM

Target Market(s)

FAMILY MEDICINE PHYSICIANS

Industry/Entity Type

MEDICAL

Font styles to use
Other font styles liked:
• CEREBRI, CODE PRO

Colors
0054AA
0677BA
7BADD7
CADEEF
E8F1F8

Requirements
Must have
• CLEAN, NEAT, CLEAR, BUT VERY PROFESSIONAL LOOK
Nice to have
• IMPROVE LAYOUT/GRAPHICS/TABLES/BOXES/DIFFERENT COLOR TEXT IN PLACES, I LIKE PAGES WITH FULL BORDER OR SPLIT PAGE INTO 2 WITH SOME GRAPHIC. ETC.
Should not have
• DONT WANT FANCY. ALL PROFESSIONAL

```html
<!DOCTYPE html>
<html lang="en">
<head>
<meta charset="utf-8">
<title>Care Halo – Physician Booklet</title>
<link rel="stylesheet" href="https://fonts.googleapis.com/css2?family=Montserrat:wght@300;400;500;600;700;800&display=swap">
<style>
:root{
  --navy:#0b4a8b;
  --navy-deep:#083c73;
  --sky:#7badd7;
  --mist:#cad8e6;
  --silver:#b7c6d8;
  --white:#ffffff;
  --ink:#1f2a36;
  --stage:#9a9c9b;
}
*{box-sizing:border-box;margin:0;padding:0}
html,body{width:1200px;height:3268px;overflow:hidden}
body{background:var(--stage);font-family:"Montserrat",sans-serif;color:var(--ink);position:relative}
.page{position:absolute;width:452px;height:585px;overflow:hidden}
.abs{position:absolute}
.header{position:absolute;left:0;top:0;width:452px;height:50px}
.contact{position:absolute;top:8px;font-size:7.5px;color:var(--white);white-space:nowrap;letter-spacing:.1px}
.contact .dot{display:inline-block;width:5px;height:5px;border:1px solid var(--white);border-radius:50%;margin:0 3px 0 6px;vertical-align:middle}
.tab-name{position:absolute;top:20px;font-size:9px;font-weight:500;color:var(--silver);letter-spacing:.5px;white-space:nowrap}
.tab-name i{display:inline-block;width:6px;height:6px;background:var(--silver);margin-right:4px;vertical-align:middle}
.photo{position:absolute;background:linear-gradient(160deg,#dfe7ee,#9fb4c8 60%,#6d8aa8)}
h2.section{font-weight:700;font-size:23px;line-height:1.2;letter-spacing:.2px}
p{font-size:9.5px;line-height:1.35}

/* cover */
.cover{left:374px;top:117px;background:var(--navy);color:var(--white);text-align:center}
.cover .brand{position:absolute;top:208px;width:100%;font-size:50px;font-weight:300;letter-spacing:1px;color:var(--silver)}
.cover .rule{position:absolute;top:298px;left:95px;width:260px;height:1px;background:var(--sky)}
.cover .tagline{position:absolute;top:322px;width:100%;font-size:18px;font-weight:400;letter-spacing:4px;line-height:1.5;color:var(--silver)}
.cover .motto{position:absolute;top:536px;width:100%;font-size:16px;font-weight:700;letter-spacing:6px}

/* spread 1 */
.founder{left:148px;top:724px;background:var(--mist)}
.founder .panel{position:absolute;left:62px;top:0;width:329px;height:585px;background:var(--navy);color:var(--white)}
.founder .name{position:absolute;top:356px;width:100%;text-align:center;font-size:10px;font-weight:700}
.founder .name span{font-weight:400}
.founder .bio{position:absolute;left:45px;top:394px;width:240px}
.founder .bio p{text-align:justify;margin-bottom:10px;font-size:9.4px}
.programs{left:600px;top:724px;background:var(--mist)}
.programs .intro{left:33px;top:64px;width:380px;font-size:8.6px}
.programs .box{position:absolute;left:0;top:104px;width:452px;height:150px;background:var(--navy);color:var(--white);padding:18px 33px}
.programs .box h2{font-size:25px;font-weight:700;line-height:1}
.programs .box .sub{font-size:8px;margin-bottom:12px}
.programs .box .item{font-size:8.2px;line-height:1.3;margin-bottom:8px}
.programs .box .item b{font-weight:700}
.programs .chart{position:absolute;left:0;top:254px;width:452px;height:240px;background:var(--white)}
.programs .outro{left:33px;top:498px;width:390px;font-size:9px;color:var(--ink)}
.programs .goal{position:absolute;top:553px;width:100%;text-align:center;font-size:11px;font-weight:600;color:var(--ink)}

/* spread 2 */
.ccm{left:148px;top:1346px;background:var(--white)}
.ccm .top{position:absolute;left:0;top:0;width:452px;height:291px;background:var(--navy);color:var(--white)}
.ccm h2{position:absolute;left:41px;top:68px;color:var(--white)}
.ccm .lede{position:absolute;left:41px;top:154px;width:200px;color:var(--white);font-size:9.6px}
.ccm .list{position:absolute;left:168px;top:304px;width:250px;list-style:none}
.ccm .list li{position:relative;padding-left:22px;font-size:9.6px;line-height:1.4;margin-bottom:11px}
.ccm .list li::before{content:"";position:absolute;left:0;top:3px;width:8px;height:8px;background:
  linear-gradient(var(--navy),var(--navy)) 0 0/3px 3px no-repeat,
  linear-gradient(var(--navy),var(--navy)) 5px 0/3px 3px no-repeat,
  linear-gradient(var(--navy),var(--navy)) 0 5px/3px 3px no-repeat,
  linear-gradient(var(--navy),var(--navy)) 5px 5px/3px 3px no-repeat}
.rpm{left:600px;top:1346px;background:var(--white)}
.rpm h2{position:absolute;left:33px;top:68px;color:var(--ink)}
.rpm .copy{position:absolute;left:33px;top:145px;width:300px}
.rpm .copy p{margin-bottom:6px;font-size:9.4px}

/* spread 3 */
.why{left:148px;top:1968px;background:var(--white)}
.why .band{position:absolute;left:0;top:0;width:329px;height:585px;background:var(--mist)}
.why h2{position:absolute;left:41px;top:82px;color:var(--ink);line-height:1.4}
.why .copy{position:absolute;left:41px;top:175px;width:228px}
.why .copy p{font-size:8.5px;line-height:1.33;margin-bottom:6px}
.costs{left:600px;top:1968px;background:var(--white)}
.costs h2{position:absolute;left:33px;top:77px;color:var(--white)}
.costs .copy{position:absolute;left:33px;top:117px;width:310px;color:var(--white);font-size:9.4px}
.costs .profit{position:absolute;left:33px;top:300px;font-size:18px;font-weight:700;color:var(--navy)}
.costs .col{position:absolute;top:352px;color:var(--navy)}
.costs .col b{display:block;font-size:13px;font-weight:700;margin-bottom:3px}
.costs .col span{display:block;font-size:13px;line-height:1.35;font-weight:400}
.costs .divider{position:absolute;left:199px;top:352px;width:1.5px;height:60px;background:var(--navy)}
.costs .bottom{position:absolute;left:0;top:464px;width:452px;height:121px;background:var(--navy)}
.costs .pay{position:absolute;top:541px;left:60px;width:392px;text-align:center;font-size:11px;font-weight:600;color:var(--white)}

/* back */
.back{left:374px;top:2596px;background:var(--navy);color:var(--white)}
.back h2{position:absolute;left:51px;top:87px;font-size:22px;font-weight:700}
.quote{position:absolute;left:0;width:452px}
.quote .avatar{position:absolute;left:51px;top:0;width:88px;height:88px;border-radius:50%;border:2px solid var(--white);background:linear-gradient(160deg,#e5e9ee,#8e9aa6)}
.quote .who{position:absolute;left:30px;top:94px;width:130px;text-align:center;font-size:9.5px;font-weight:700}
.quote .who small{display:block;font-size:6.5px;font-weight:600}
.quote p{position:absolute;left:173px;top:2px;width:230px;font-size:9.4px;line-height:1.33}
</style>
</head>
<body>

<!-- Cover -->
<section class="page cover">
  <div class="brand">CARE HALO</div>
  <div class="rule"></div>
  <div class="tagline">CHRONIC CARE<br>EXPERTS</div>
  <div class="motto">SAVING LIVES 24/7</div>
</section>

<!-- Spread 1 left: founder -->
<section class="page founder">
  <div class="panel">
    <div class="photo" role="img" aria-label="Family portrait of the founder on a beach" style="left:45px;top:56px;width:238px;height:287px"></div>
    <div class="name">Dale Whitford, <span>RN, BSN</span></div>
    <div class="bio">
      <p>Started <b>Care Halo</b> One, LLC in 2022 to provide Chronic Care Services with the mission to help people stay at home and out of the hospital. His first job was an orderly in the hospital at age 17.</p>
      <p>In the past 35 years, he has successfully started, grown, and sold a Physical Therapy clinic, a Home Medical Equipment company, and a Sleep Lab.</p>
      <p>From 2015 to 2022, he worked as a Critical Care Travel Nurse in 5 states.</p>
    </div>
  </div>
</section>

<!-- Spread 1 right: programs -->
<section class="page programs">
  <svg class="header" viewBox="0 0 452 50" aria-hidden="true">
    <path d="M0,0H452V42H352Q344,42 340,34L334,26H0Z" fill="var(--navy)"/>
    <path d="M0,29H332L337,37Q342,46 352,46H452" fill="none" stroke="var(--silver)" stroke-width="2"/>
  </svg>
  <div class="contact" style="left:30px"><span class="dot"></span>dale@carehalo918.com<span class="dot"></span>carehalo918.com</div>
  <div class="tab-name" style="right:14px"><i></i>CARE HALO</div>
  <p class="abs intro">CMS created Chronic Care Management (CCM) in 2015 to improve quality of healthcare and reduce hospital visits which lowers overall healthcare related costs. Statistics show up to 50% cost reduction in patients enrolled in CCM.</p>
  <div class="box">
    <h2>OUR PROGRAMS</h2>
    <div class="sub">(Enrollment % of your total Medicare Population)</div>
    <div class="item"><b>Chronic Care Management</b><br>2 Chronic Conditions <b>(80% Enrollment)</b></div>
    <div class="item"><b>Remote Patient Monitoring (RPM)</b><br>BP, Pulse Ox, Glucometer, Scale <b>(70% Enrollment)</b></div>
    <div class="item"><b>Behavioral Health (BHI)</b><br>1 Mental Health condition <b>(60% Enrollment)</b></div>
  </div>
  <svg class="chart" viewBox="0 0 452 240" role="img" aria-label="Bar chart of chronic condition prevalence over 65 years">
    <text x="226" y="18" text-anchor="middle" font-family="Montserrat,sans-serif" font-size="12.5" font-weight="700" fill="var(--navy)">Chronic Condition Prevalence &gt; 65 yrs</text>
    <g stroke="#b9bec4" stroke-width="1">
      <line x1="86" y1="36" x2="86" y2="218"/><line x1="190" y1="36" x2="190" y2="218"/>
      <line x1="293" y1="36" x2="293" y2="218"/><line x1="397" y1="36" x2="397" y2="218"/>
    </g>
    <g fill="var(--silver)">
      <rect x="86" y="41" width="299" height="8"/><rect x="86" y="59" width="207" height="8"/>
      <rect x="86" y="77" width="174" height="8"/><rect x="86" y="96" width="174" height="8"/>
      <rect x="86" y="114" width="174" height="8"/><rect x="86" y="132" width="141" height="8"/>
      <rect x="86" y="151" width="141" height="8"/><rect x="86" y="169" width="104" height="8"/>
      <rect x="86" y="187" width="91" height="8"/><rect x="86" y="206" width="91" height="8"/>
    </g>
    <g font-family="Montserrat,sans-serif" font-size="6.5" font-weight="700" fill="var(--navy)" text-anchor="end">
      <text x="81" y="48">HTN</text><text x="81" y="66">HLD</text><text x="81" y="84">CKD</text>
      <text x="81" y="103">OBESITY</text><text x="81" y="121">MEMORY</text><text x="81" y="139">DIABETES</text>
      <text x="81" y="158">PAIN</text><text x="81" y="176">CANCER</text><text x="81" y="194">COPD</text><text x="81" y="213">CHF</text>
    </g>
    <g font-family="Montserrat,sans-serif" font-size="6.5" fill="#555" text-anchor="middle">
      <text x="86" y="228">0%</text><text x="190" y="228">25%</text><text x="293" y="228">50%</text><text x="397" y="228">75%</text>
    </g>
  </svg>
  <p class="abs outro">Care Halo maximizes access to all available resources, minimizes barriers to compliance, and encourages positive lifestyle choices. Our nurses are personal advocates for your clients.</p>
  <div class="goal">Our # 1 Goal is to prevent MIs and CVAs.</div>
</section>

<!-- Spread 2 left: CCM / BHI -->
<section class="page ccm">
  <div class="top"></div>
  <svg class="header" viewBox="0 0 452 50" aria-hidden="true">
    <g transform="translate(452,0) scale(-1,1)">
      <path d="M0,0H452V42H352Q344,42 340,34L334,26H0Z" fill="var(--navy)"/>
      <path d="M0,29H332L337,37Q342,46 352,46H452" fill="none" stroke="var(--silver)" stroke-width="2"/>
    </g>
  </svg>
  <div class="contact" style="right:30px"><span class="dot"></span>dale@carehalo918.com<span class="dot"></span>carehalo918.com</div>
  <div class="tab-name" style="left:14px"><i></i>CARE HALO</div>
  <h2 class="section">CCM- CHRONIC CARE<br>BHI-BEHAVIORAL HEALTH</h2>
  <p class="lede">Registered Nurse will be accessible by phone 24 / 7 for addressing patient needs such as assessments, refills, education, and expediting sick visits.</p>
  <div class="photo" role="img" aria-label="Hand holding a desk telephone receiver" style="left:266px;top:164px;width:145px;height:127px;background:linear-gradient(150deg,#3d4f63,#1d2733 55%,#c99a7c)"></div>
  <ul class="list">
    <li>Assisting in referrals to specialists and home care services.</li>
    <li>Assisting with social services, transportation, and medical equipment and supplies.</li>
    <li>Scheduling any preventive care needed.</li>
    <li>Providing nutritional education and supporting positive lifestyle changes.</li>
  </ul>
  <svg class="abs" style="left:0;top:440px" width="452" height="145" viewBox="0 0 452 145" aria-hidden="true">
    <path d="M452,22H150Q112,22 102,50Q92,85 40,85H0V145H452Z" fill="var(--navy)"/>
    <g fill="none" stroke="var(--sky)" stroke-width="1">
      <circle cx="197" cy="71" r="19"/><circle cx="255" cy="71" r="19"/>
      <circle cx="315" cy="71" r="19"/><circle cx="373" cy="71" r="19"/>
    </g>
    <g font-family="Montserrat,sans-serif" font-size="7" fill="var(--sky)" text-anchor="middle">
      <text x="197" y="74">ICON</text><text x="255" y="74">ICON</text><text x="315" y="74">ICON</text><text x="373" y="74">ICON</text>
    </g>
  </svg>
</section>

<!-- Spread 2 right: RPM -->
<section class="page rpm">
  <svg class="abs" style="left:0;top:0" width="452" height="585" viewBox="0 0 452 585" aria-hidden="true">
    <path d="M0,0H452V246Q365,246 350,285Q335,324 295,324H0Z" fill="var(--mist)"/>
    <rect x="0" y="529" width="452" height="56" fill="var(--mist)"/>
  </svg>
  <svg class="header" viewBox="0 0 452 50" aria-hidden="true">
    <path d="M0,0H452V42H352Q344,42 340,34L334,26H0Z" fill="var(--navy)"/>
    <path d="M0,29H332L337,37Q342,46 352,46H452" fill="none" stroke="var(--silver)" stroke-width="2"/>
  </svg>
  <div class="contact" style="left:30px"><span class="dot"></span>dale@carehalo918.com<span class="dot"></span>carehalo918.com</div>
  <div class="tab-name" style="right:14px"><i></i>CARE HALO</div>
  <h2 class="section">RPM- REMOTE PATIENT<br>MONITORING</h2>
  <div class="copy">
    <p>Remote monitoring devices are provided which track blood pressure, weight, oxygen, glucose and automatically upload to our software sending us alerts in real time. Alerts are monitored and addressed 24/7.</p>
    <p>RN's provide critical thinking and assessments for patients around the clock.</p>
    <p>If intervention is needed we notify provider with data for new meds, sick visit, or referral to urgent/emergent care. Notifications to providers and staff are sent as telephone encounters via CLX for seamless communication from nurses to provider.</p>
  </div>
  <div class="photo" role="img" aria-label="Remote monitoring devices: blood pressure cuff, pulse oximeter, glucometer and scale" style="left:30px;top:341px;width:296px;height:171px;background:linear-gradient(135deg,#5b6168,#e6e9ec 45%,#f4f5f6 70%,#c6ccd2)"></div>
</section>

<!-- Spread 3 left: why -->
<section class="page why">
  <div class="band"></div>
  <svg class="header" viewBox="0 0 452 50" aria-hidden="true">
    <g transform="translate(452,0) scale(-1,1)">
      <path d="M0,0H452V42H352Q344,42 340,34L334,26H0Z" fill="var(--navy)"/>
      <path d="M0,29H332L337,37Q342,46 352,46H452" fill="none" stroke="var(--silver)" stroke-width="2"/>
    </g>
  </svg>
  <div class="contact" style="right:30px"><span class="dot"></span>dale@carehalo918.com<span class="dot"></span>carehalo918.com</div>
  <div class="tab-name" style="left:14px"><i></i>CARE HALO</div>
  <h2 class="section">WHY CARE HALO?<br>WE STAFF LOCAL RN'S</h2>
  <div class="copy">
    <p>Care Halo guarantees a dedicated team of Critical Care RN's, LPN's and Medical Assistants. We continue to build our team with the most experienced and passionate advocates to ensure the absolute best service for your clients.</p>
    <p>Care Halo bridges the gap between clinical and home environments. We prioritize following up and following through which results in better coordination of care and the best possible outcomes.</p>
    <p>We maintain 100% compliance with Annual Wellness Visits. Maintaining the highest standards is a priority for our team and is what sets us apart from other Chronic Care Providers.</p>
    <p>Using CLX guarantees seamless integration into your practice. The GOAL is for clients to call CCM 24/7 phone instead of main office for all needs. This eliminates non-billable staff time.</p>
    <p>Our average monthly reimbursement is $125 greater than the national average because we believe in spending as much time with our patients as needed.</p>
    <p>Our daily average is 70 outgoing calls and 40 incoming calls. We typically respond to 65 RPM alerts and 10 Telephone Encounters daily. We send several patients to ER weekly.</p>
  </div>
</section>

<!-- Spread 3 right: costs -->
<section class="page costs">
  <svg class="abs" style="left:0;top:0" width="452" height="260" viewBox="0 0 452 260" aria-hidden="true">
    <path d="M0,0H452V180Q335,180 310,222Q292,259 255,259H0Z" fill="var(--navy)"/>
  </svg>
  <svg class="header" viewBox="0 0 452 50" aria-hidden="true">
    <path d="M0,0H452V42H352Q344,42 340,34L334,26H0Z" fill="var(--navy)"/>
    <path d="M0,29H332L337,37Q342,46 352,46H452" fill="none" stroke="var(--silver)" stroke-width="2"/>
  </svg>
  <div class="contact" style="left:30px"><span class="dot"></span>dale@carehalo918.com<span class="dot"></span>carehalo918.com</div>
  <div class="tab-name" style="right:14px"><i></i>CARE HALO</div>
  <h2 class="section">START UP COSTS</h2>
  <p class="copy">Care Halo covers all up front costs including CLX, clinical and billing staff, providers' staff orientation, and all marketing materials (mass email, magnetic business cards with 24/7 phone number, brochures, posters, and webpage for your current website).<br><b>RPM devices will cost over $100,000.</b></p>
  <div class="profit">Monthly Net Profit per 1000 clients</div>
  <div class="col" style="left:33px"><b>Building Phase</b><span>First 6 months $50,000<br>($50 per patient)</span></div>
  <div class="divider"></div>
  <div class="col" style="left:225px"><b>Management Phase</b><span>After 6 months $100,000<br>($100 per patient)</span></div>
  <div class="bottom"></div>
  <div class="pay">Care Halo gets paid after Medicare pays you!</div>
</section>

<!-- Back: testimonials -->
<section class="page back">
  <div class="contact" style="right:24px;top:20px"><span class="dot"></span>dale@carehalo918.com<span class="dot"></span>carehalo918.com</div>
  <h2>HAPPY PATIENTS...</h2>
  <div class="quote" style="top:145px">
    <div class="avatar" role="img" aria-label="Portrait of a patient"></div>
    <div class="who">Rena Adair<small>Product Designer</small></div>
    <p>Booklets are printed materials with four or more pages, containing details about a business, event, product, promotion, etc. They are also known as catalogs or pamphlets, and are usually created to communicate a message to a wide variety of audiences.</p>
  </div>
  <div class="quote" style="top:278px">
    <div class="avatar" role="img" aria-label="Portrait of a patient"></div>
    <div class="who">Tomas Brill<small>Marketer</small></div>
    <p>Booklets are printed materials with four or more pages, containing details about a business, event, product, promotion, etc. They are also known as catalogs or pamphlets, and are usually created to communicate a message to a wide variety of audiences.</p>
  </div>
  <div class="quote" style="top:418px">
    <div class="avatar" role="img" aria-label="Portrait of a patient"></div>
    <div class="who">Lena Okafor<small>Graphic Designer</small></div>
    <p>Booklets are printed materials with four or more pages, containing details about a business, event, product, promotion, etc. They are also known as catalogs or pamphlets, and are usually created to communicate a message to a wide variety of audiences.</p>
  </div>
</section>

</body>
</html>
```